Book cover needed for Christian Non-Fiction Book

I need book cover design (eBook , Paperback, and possibly case laminate Hardcover) for use on Folvane Press and Corvel Print.
Title: Bound for Shore
Sub-Title: Leaving Harbors and Walking in Quiet Trust
Author: Neil Varden
Also on front cover "Forward by R. Leona Pask"

I like clean/simple designs. Below are links to examples of covers I like...
https://www.shelvora.example/dp/Q4821MZT0X?tag=kelvpage-20&linkCode=ogi&th=1&psc=1
https://www.shelvora.example/dp/Q48HTRNWAC?tag=kelvpage-20&linkCode=ogi&th=1&psc=1
https://www.shelvora.example/dp/Q22FKD93XJ?tag=kelvpage-20&linkCode=ogi&th=1&psc=1
https://www.shelvora.example/dp/Q48W3PLMHD?tag=kelvpage-20&linkCode=ogi&th=1&psc=1
https://www.shelvora.example/dp/Q48R5ZZCQN?tag=kelvpage-20&linkCode=ogi&th=1&psc=1
https://www.shelvora.example/dp/Q22H0KKPU7?tag=kelvpage-20&linkCode=ogi&th=1&psc=1

The main idea for Bound for Shore is that God is a sending God and being "on the move" or journeying is central to God's character, and therefore God's people. I write about our hesitancy to "go," and how the Bible is full of stories about people "going" from Abraham to Jesus, to the disciples of Jesus.

The core biblical text is the Great Commission in Matthew 28:16-20, where Jesus sends out his followers, though some of them doubt.

This paragraph from the forward by R. Leona Pask captures the tone of the book well:
This book is a call amid the turmoil. Sacred scripture contains no shortage of narratives in which humans are pulled from their ordinary lives with an inciting incident whose stakes are high. These Biblical figures are lulled from complacency and comfort zones—and yet they are reluctant to serve because they question their ability and influence. Their lessons are relevant for us today: They, and we, are always called and sent with authority. The power of the Holy Spirit equips their “going”—and ours. It’s a sending out that looks less like mastery and more humility. It’s a sending out that is unequivocal service to others modelled in a rabbi-reformer who washed feet and touched the unclean.

I have previously published two shorter books and would be very interested in getting new covers for the old books these so that the three have a similar feel. Whichever designer I go with for "Bound for Shore" I would also want to work with on creating a "branded look" for the other two books.

Target Market(s)

Christian, Religion, Spirituality Readers

Requirements
Must have
• The front cover must have this copy...
Bound for Shore
Leaving Harbors and Walking in Quiet Trust
Neil Varden
Forward by R. Leona Pask

Must be willing to do the full paperback and/or hardcover, but start with thefront cover please
Nice to have
• See attached files for some book covers I like

```html
<!DOCTYPE html>
<html lang="en">
<head>
<meta charset="utf-8">
<title>Bound for Shore — Neil Varden</title>
<link rel="stylesheet" href="https://fonts.googleapis.com/css2?family=Marcellus&family=Sorts+Mill+Goudy&display=swap">
<style>
  :root {
    --cover-stone: #b7b3ab;
    --ink: #0d0c0b;
    --leaf: #4f9a2c;
    --leaf-soft: #8fa77f;
  }
  html, body {
    margin: 0;
    padding: 0;
    width: 800px;
    height: 1200px;
    overflow: hidden;
    background: var(--cover-stone);
  }
  .cover {
    position: relative;
    width: 800px;
    height: 1200px;
    background: var(--cover-stone);
    color: var(--ink);
    text-align: center;
  }
  .title {
    position: absolute;
    top: 104px;
    left: 0;
    width: 100%;
    margin: 0;
    font-family: "Marcellus", serif;
    font-weight: 400;
    font-size: 76px;
    line-height: 1;
    letter-spacing: 1px;
    text-transform: uppercase;
  }
  .subtitle {
    position: absolute;
    top: 202px;
    left: 90px;
    width: 620px;
    margin: 0;
    font-family: "Sorts Mill Goudy", serif;
    font-size: 34px;
    line-height: 40px;
    font-weight: 400;
  }
  .cover-art {
    position: absolute;
    left: 262px;
    top: 446px;
    width: 276px;
    height: 570px;
    background: linear-gradient(to bottom, var(--leaf) 0%, var(--leaf-soft) 65%, var(--cover-stone) 100%);
  }
  .author {
    position: absolute;
    top: 1046px;
    left: 0;
    width: 100%;
    margin: 0;
    font-family: "Sorts Mill Goudy", serif;
    font-size: 50px;
    line-height: 1;
    font-weight: 400;
  }
  .foreword {
    position: absolute;
    top: 1128px;
    left: 0;
    width: 100%;
    margin: 0;
    font-family: "Sorts Mill Goudy", serif;
    font-size: 29px;
    line-height: 1;
    letter-spacing: 9px;
  }
</style>
</head>
<body>
  <main class="cover">
    <h1 class="title">Bound for Shore</h1>
    <p class="subtitle">Leaving Harbors and Walking in Quiet Trust</p>
    <div class="cover-art" role="img" aria-label="Photograph of a single leafy green tree standing alone, its reflection fading into mist below"></div>
    <p class="author">Neil Varden</p>
    <p class="foreword">Forward by R. Leona Pask</p>
  </main>
</body>
</html>
```